Tuscan Wine Producer Needs a New Label for Chianti Bottle

We are looking to re-design the label for our Chianti bottle.

The aim is to obtain a label that plays on the estate's history and Tuscan heritage, however with a modern twist.

Please see full brief, estate logo, text to be included on the label and pictures of the estate

```html
<!DOCTYPE html>
<html lang="it">
<head>
<meta charset="utf-8">
<title>Villa Serenella – Chianti 1014 Label</title>
<link href="https://fonts.googleapis.com/css2?family=Cormorant+Garamond:wght@400;500&family=Pinyon+Script&display=swap" rel="stylesheet">
<style>
  :root {
    --page: #ffffff;
    --label: #ffffff;
    --ink: #2b2b2b;
    --wine-red: #d3202a;
    --engraving-dark: #5a5a5a;
    --engraving-light: #c9c9c9;
  }
  * { margin: 0; padding: 0; box-sizing: border-box; }
  html, body {
    width: 1200px;
    height: 1000px;
    overflow: hidden;
    background: var(--page);
  }
  .canvas {
    position: relative;
    width: 1200px;
    height: 1000px;
  }
  .label {
    position: absolute;
    left: 415px;
    top: 233px;
    width: 370px;
    height: 534px;
    background: var(--label);
    box-shadow: 0 2px 8px rgba(0, 0, 0, 0.18);
  }
  .estate-name {
    position: absolute;
    top: 91px;
    left: 0;
    width: 100%;
    text-align: center;
    font-family: "Cormorant Garamond", serif;
    font-weight: 500;
    font-size: 15px;
    letter-spacing: 1.5px;
    text-transform: uppercase;
    color: var(--ink);
  }
  .ornament {
    position: absolute;
    left: 181px;
    width: 8px;
    height: 10px;
    border-radius: 2px;
    background: var(--wine-red);
  }
  .ornament--top { top: 171px; }
  .ornament--bottom { top: 331px; }
  .wine-name {
    position: absolute;
    top: 192px;
    left: 0;
    width: 100%;
    text-align: center;
    font-family: "Pinyon Script", cursive;
    font-weight: 400;
    font-size: 54px;
    line-height: 1;
    color: var(--wine-red);
    white-space: nowrap;
  }
  .divider {
    position: absolute;
    top: 262px;
    left: 175px;
    width: 20px;
    height: 1.5px;
    background: var(--ink);
  }
  .appellation {
    position: absolute;
    top: 283px;
    left: 0;
    width: 100%;
    text-align: center;
    font-family: "Cormorant Garamond", serif;
    font-size: 11.5px;
    line-height: 17px;
    letter-spacing: 0.8px;
    text-transform: uppercase;
    color: var(--ink);
  }
  .estate-view {
    position: absolute;
    top: 374px;
    left: 100px;
    width: 158px;
    height: 100px;
    border-radius: 40% 50% 30% 30%;
    background: radial-gradient(ellipse at 50% 55%, var(--engraving-dark) 0%, #8a8a8a 45%, var(--engraving-light) 75%, rgba(255,255,255,0) 100%);
  }
</style>
</head>
<body>
  <main class="canvas">
    <section class="label">
      <p class="estate-name">Villa Serenella</p>
      <div class="ornament ornament--top" role="img" aria-label="Small red fleur-de-lis ornament"></div>
      <h1 class="wine-name">Chianti 1014</h1>
      <div class="divider"></div>
      <p class="appellation">Denominazione di origine<br>controllata e garantita</p>
      <div class="ornament ornament--bottom" role="img" aria-label="Small red fleur-de-lis ornament"></div>
      <div class="estate-view" role="img" aria-label="Engraved illustration of the estate villa beside a row of tall trees"></div>
    </section>
  </main>
</body>
</html>
```